O Balcão KEZ - costumer paper bag

We need a new design for the paper bags of our stores located in Portugal (Funchal and Lisboa).
The design must use logo colors. The final design should comunicate top fashion image, glamour and exclusivity.
We are a gowns and accessories speciality store with 4 fisical locations and online at www.obalcao.pt

Target Market(s)

Mass market, up scale consumers

Industry/Entity Type

Kez

Requirements
Must have
• . keep diamonds in logo of the letters KEZ
• . simple design
• - work only with the colors black, white, silver
• - modern
Nice to have
• elegante and simple design
Should not have
• differente colors other of the mentioned above
• complicated desing

```html
<!DOCTYPE html>
<html lang="pt">
<head>
<meta charset="utf-8">
<title>O Balcão KEZ — Saco de compras</title>
<link rel="stylesheet" href="https://fonts.googleapis.com/css2?family=Quicksand:wght@500&family=Archivo+Black&display=swap">
<style>
  :root {
    --bg: #a9a8aa;
    --bag-black: #0a0a0a;
    --bag-white: #f4f4f4;
    --silver: #c9c9cc;
    --text-white: #ffffff;
  }
  * { margin: 0; padding: 0; box-sizing: border-box; }
  html, body {
    width: 1200px;
    height: 1200px;
    overflow: hidden;
    background: var(--bg);
  }
  .canvas {
    position: relative;
    width: 1200px;
    height: 1200px;
  }
  .bag-face {
    position: absolute;
    left: 50px;
    top: 224px;
    width: 1100px;
    height: 752px;
    background: var(--bag-black);
    overflow: hidden;
  }
  .ornament-panel {
    position: absolute;
    inset: 0;
    width: 100%;
    height: 100%;
  }
  .brand-box {
    position: absolute;
    left: 46px;
    top: 67px;
    width: 538px;
    height: 89px;
    border: 3px solid var(--text-white);
    display: flex;
    align-items: center;
    justify-content: center;
  }
  .brand-name {
    font-family: "Quicksand", sans-serif;
    font-weight: 500;
    font-size: 66px;
    line-height: 1;
    color: var(--text-white);
    letter-spacing: 1px;
  }
  .tier-mark {
    position: absolute;
    left: 66px;
    top: 560px;
    font-family: "Archivo Black", sans-serif;
    font-size: 172px;
    line-height: 1;
    color: var(--silver);
    letter-spacing: 2px;
  }
</style>
</head>
<body>
  <main class="canvas">
    <section class="bag-face">
      <svg class="ornament-panel" viewBox="0 0 1100 752" preserveAspectRatio="none">
        <path d="M880 0 C790 110 700 260 730 430 C750 560 640 700 560 752 L1100 752 L1100 0 Z"
              fill="var(--bag-white)" role="img"
              aria-label="Flowing black floral swirl ornament with curling tendrils and small leaves on a white sweep"/>
        <path d="M855 0 C765 110 675 260 705 430 C725 560 615 700 535 752"
              fill="none" stroke="var(--bag-white)" stroke-width="4"/>
      </svg>
      <div class="brand-box">
        <span class="brand-name">O Balcão</span>
      </div>
      <div class="tier-mark">KEZ</div>
    </section>
  </main>
</body>
</html>
```